Website for an interior designer

We need a new website for Clara Beth Holloway whose new business name is Clara Beth Holloway Interiors. She is a residential interior designer with a mix of modern and contemporary tastes. We are in the process of overhauling her website which is +15 years old and not an accurate reflection of her tastes. The uploaded photos are from some of the houses she has done as well as her logo(s). We would need a section for "About Us" that would have a paragraph of text and bullets showing services and a gallery for photos (~12 total, more to come). A contract page would be optional. The client likes the feel/look of this website: https://www.pondrickstudio.example/ but doesn't want to copy it exactly.

Target Market(s)

Upscale home owners

Industry/Entity Type

Interior Design

Coding

Coded - Design and coding required

Number of Pages Required

4 page

Colors

Designer to choose only greyscale colors for use in the design.

Requirements
Must have
• Home page, about us page, gallery page, contact us page.

```html
<!DOCTYPE html>
<html lang="en">
<head>
<meta charset="utf-8">
<title>Clara Beth Holloway Interiors</title>
<link rel="stylesheet" href="https://fonts.googleapis.com/css2?family=Cormorant+Garamond:wght@300;400;500&family=Crimson+Text:wght@400;600&display=swap">
<style>
:root{
  --ink:#3e3e3e;
  --ink-soft:#666666;
  --slate:#5f5f5f;
  --footer:#4b4b4b;
  --footer-bar:#3a3a3a;
  --paper:#ffffff;
  --rule:#9a9a9a;
  --white:#ffffff;
  --light:#eeeeee;
  --deco:#e6e6e6;
  --head:'Cormorant Garamond', Georgia, serif;
  --body:'Crimson Text', Georgia, serif;
}
*{box-sizing:border-box;margin:0;padding:0}
html,body{width:1200px;height:4348px;overflow:hidden}
body{position:relative;background:var(--paper);color:var(--ink);font-family:var(--body);-webkit-font-smoothing:antialiased;-moz-osx-font-smoothing:grayscale;text-rendering:geometricPrecision}
.abs{position:absolute}
a{color:inherit;text-decoration:none}

/* hero */
.hero{left:0;top:0;width:1200px;height:1061px;background:linear-gradient(160deg,#f6f6f6 0%,#efefef 55%,#f4f4f4 100%)}
.hero-deco{left:0;top:0;width:1200px;height:1061px}
.social-top{top:9px;left:0;width:1200px;display:flex;justify-content:center;gap:46px}
.dot-icon{width:14px;height:14px;border:1.5px solid #999999;border-radius:50%}
.brand{top:88px;left:0;width:1200px;text-align:center;color:var(--ink)}
.brand-mark{font-family:var(--head);font-weight:300;font-size:64px;letter-spacing:4px;line-height:1;color:var(--ink)}
.brand-name{font-family:var(--head);font-weight:500;font-size:29px;letter-spacing:3px;margin-top:14px;color:var(--ink)}
.brand-sub{display:flex;justify-content:center;align-items:center;gap:14px;font-family:var(--head);font-weight:500;font-size:14px;letter-spacing:8px;margin-top:6px;color:var(--ink)}
.brand-sub span.line{width:44px;height:1.5px;background:var(--ink)}
.nav{top:290px;left:0;width:1200px;display:flex;justify-content:center;gap:42px;font-family:var(--head);font-weight:500;font-size:19px;letter-spacing:3.5px;color:#555555}
.nav a.active{border-bottom:1.5px solid #555555;padding-bottom:3px}
.hero-band{left:0;top:413px;width:517px;height:509px;background:var(--slate)}
.hero-photo{left:98px;top:450px;width:522px;height:435px;background:linear-gradient(180deg,#f4f4f4 0%,#e3e3e3 60%,#969696 100%)}
.hero-title{left:676px;top:516px;font-family:var(--head);font-weight:400;font-size:56px;line-height:60px;letter-spacing:4px;color:#4a4a4a}
.hero-rule{left:676px;top:641px;width:524px;height:1.5px;background:var(--rule)}
.hero-text{left:676px;top:667px;width:410px;font-size:18px;line-height:24px;letter-spacing:1px;color:var(--ink-soft)}
.btn{display:inline-block;background:var(--slate);color:var(--white);font-family:var(--body);letter-spacing:1.5px}
.hero-btn{left:676px;top:754px;width:150px;height:52px;line-height:52px;text-align:center;font-size:18px}

/* about */
.about-block{left:870px;top:1130px;width:330px;height:679px;background:var(--slate)}
.about-photo-1{left:670px;top:1159px;width:300px;height:356px;background:linear-gradient(100deg,#e2e2e2 0%,#f0f0f0 40%,#777777 80%,#393939 100%)}
.about-photo-2{left:802px;top:1420px;width:298px;height:356px;background:linear-gradient(180deg,#f4f4f4 0%,#e4e4e4 60%,#bbbbbb 100%)}
.about-title{left:120px;top:1262px;font-family:var(--head);font-weight:400;font-size:48px;letter-spacing:1px;color:#4a4a4a}
.about-rule{left:120px;top:1320px;width:428px;height:1.5px;background:var(--rule)}
.about-text{left:120px;top:1350px;width:428px;font-size:18px;line-height:24.5px;color:#555555;text-align:justify}
.about-btn{left:120px;top:1611px;width:147px;height:52px;line-height:52px;text-align:center;font-size:18px}

/* services */
.services{left:0;top:1863px;width:1200px;height:952px;background:linear-gradient(135deg,#f6f6f6 0%,#ededed 50%,#f5f5f5 100%)}
.section-title{left:0;width:1200px;text-align:center;font-family:var(--head);font-weight:400;font-size:50px;letter-spacing:1px;color:#4a4a4a}
.section-sub{left:0;width:1200px;text-align:center;font-size:19px;line-height:24px;letter-spacing:1.5px;color:var(--ink-soft)}
.dots{top:2161px;left:0;width:1200px;display:flex;justify-content:center;gap:4px}
.dots i{width:12px;height:12px;border-radius:50%;background:#555555;border:2px solid #555555}
.dots i.off{background:var(--white)}
.card{top:2215px;width:322px;height:424px}
.card-photo{position:absolute;left:0;top:0;width:322px;height:311px}
.card-body{position:absolute;left:0;top:311px;width:322px;height:113px;padding:22px 20px 0;font-size:13px;line-height:17px;letter-spacing:1px;background:var(--slate);color:var(--white)}
.card.light .card-body{background:var(--white);color:#666666}
.card-btn{position:absolute;left:50%;top:405px;transform:translateX(-50%);width:116px;height:34px;line-height:34px;text-align:center;font-size:13px;letter-spacing:1px;background:var(--white);color:#555555}
.card.light .card-btn{background:var(--slate);color:var(--white)}

/* gallery */
.tile{overflow:hidden}
.tile-label{position:absolute;left:0;top:0;width:100%;height:100%;display:flex;align-items:center;justify-content:center;font-family:var(--head);font-weight:500;font-size:32px;color:var(--white);background:rgba(70,70,70,.55);letter-spacing:.5px}

/* footer */
.footer{left:0;top:3852px;width:1200px;height:453px;background:var(--footer)}
.footer-bar{left:0;top:4305px;width:1200px;height:43px;background:var(--footer-bar);color:#dddddd;text-align:center;line-height:43px;font-size:15px;letter-spacing:4px}
.foot-mark{left:128px;top:3950px;font-family:var(--head);font-weight:300;font-size:78px;letter-spacing:3px;line-height:1;color:var(--white)}
.foot-text{left:120px;top:4066px;width:350px;font-size:14px;line-height:24px;color:var(--light)}
.foot-social{left:124px;top:4194px;display:flex;gap:26px}
.foot-social .dot-icon{border-color:#dddddd;width:18px;height:18px}
.foot-col{top:3980px;color:var(--white)}
.foot-col h4{font-family:var(--head);font-weight:500;font-size:25px;letter-spacing:.3px;margin-bottom:40px;color:var(--white)}
.foot-col ul{list-style:none;font-size:14px;line-height:34px;color:var(--light)}
.foot-col li::before{content:"›";font-size:20px;margin-right:12px;color:var(--light)}
.foot-contact p{font-size:14px;line-height:18px;color:var(--light);margin-bottom:14px}
</style>
</head>
<body>

<section class="hero abs">
  <svg class="hero-deco abs" viewBox="0 0 1200 1061" aria-hidden="true">
    <g fill="none" stroke="#e6e6e6" stroke-width="1.5">
      <rect x="860" y="40" width="280" height="440"/>
      <line x1="1000" y1="40" x2="1000" y2="480"/>
      <line x1="860" y1="260" x2="1140" y2="260"/>
      <rect x="60" y="900" width="260" height="161"/>
    </g>
  </svg>
  <div class="social-top abs"><span class="dot-icon"></span><span class="dot-icon"></span><span class="dot-icon"></span><span class="dot-icon"></span></div>
  <div class="brand abs">
    <div class="brand-mark">CBH</div>
    <div class="brand-name">CLARA BETH HOLLOWAY</div>
    <div class="brand-sub"><span class="line"></span>INTERIORS<span class="line"></span></div>
  </div>
  <nav class="nav abs">
    <a class="active" href="#">HOME</a><a href="#">ABOUT US</a><a href="#">SERVICES</a><a href="#">GALLERY</a><a href="#">CONTACT US</a>
  </nav>
  <div class="hero-band abs"></div>
  <div class="hero-photo abs" role="img" aria-label="Bright white living room with tall black-framed windows, cream sofas and a wooden coffee table"></div>
  <h1 class="hero-title abs">STATE<br>OF THE ART</h1>
  <div class="hero-rule abs"></div>
  <p class="hero-text abs">Lorem Ipsum is simply dummy text of the printing and typesetting industry.</p>
  <a class="btn hero-btn abs" href="#">Read More</a>
</section>

<section class="about">
  <div class="about-block abs"></div>
  <div class="about-photo-1 abs" role="img" aria-label="Staircase with colorful painted risers beside an abstract painting"></div>
  <div class="about-photo-2 abs" role="img" aria-label="White stairwell with a black railing and a tall window"></div>
  <h2 class="about-title abs">ABOUT US</h2>
  <div class="about-rule abs"></div>
  <p class="about-text abs">Lorem ipsum dolor sit amet, consectetur adipiscing elit, sed do eiusmod tempor incididunt ut labore et dolore magna aliqua. Quis ipsum suspendisse ultrices gravida. Risus commodo viverra maecenas accumsan lacus vel facilisis. Lorem ipsum dolor sit amet, consectetur adipiscing elit, sed do eiusmod tempor incididunt ut labore et dolore magna aliqua. Quis ipsum suspendisse ultrices gravida. Risus commodo viverra maecenas accumsan lacus vel facilisis.</p>
  <a class="btn about-btn abs" href="#">Read More</a>
</section>

<section class="services abs"></section>
<h2 class="section-title abs" style="top:1984px">SERVICES</h2>
<p class="section-sub abs" style="top:2076px">Lorem Ipsum is simply dummy text of the<br>printing and typesetting industry.</p>
<div class="dots abs"><i></i><i class="off"></i><i></i></div>

<article class="card abs" style="left:98px">
  <div class="card-photo" role="img" aria-label="White modern kitchen with a glass table and a red vase" style="background:linear-gradient(180deg,#efefef 0%,#e0e0e0 70%,#b3b3b3 100%)"></div>
  <p class="card-body">Lorem Ipsum is simply dummy text of the printing and typesetting industry.</p>
  <a class="card-btn" href="#">Read More</a>
</article>
<article class="card light abs" style="left:439px">
  <div class="card-photo" role="img" aria-label="Dim contemporary kitchen with dark cabinetry and wood counter" style="background:linear-gradient(180deg,#707070 0%,#5b5b5b 60%,#747474 100%)"></div>
  <p class="card-body">Lorem Ipsum is simply dummy text of the printing and typesetting industry.</p>
  <a class="card-btn" href="#">Read More</a>
</article>
<article class="card abs" style="left:780px">
  <div class="card-photo" role="img" aria-label="Pale wall hung with framed posters and prints" style="background:linear-gradient(180deg,#e6e6e6 0%,#d9d9d9 100%)"></div>
  <p class="card-body">Lorem Ipsum is simply dummy text of the printing and typesetting industry.</p>
  <a class="card-btn" href="#">Read More</a>
</article>

<h2 class="section-title abs" style="top:2917px">GALLERY</h2>
<p class="section-sub abs" style="top:3009px">Lorem Ipsum is simply dummy text of the<br>printing and typesetting industry.</p>

<div class="tile abs" role="img" aria-label="Grey sofa with dark and patterned cushions" style="left:104px;top:3163px;width:237px;height:520px;background:linear-gradient(180deg,#e5e5e5 0%,#cecece 60%,#909090 100%)"></div>
<div class="tile abs" style="left:350px;top:3163px;width:250px;height:257px;background:linear-gradient(180deg,#8e8e8e,#6c6c6c)" role="img" aria-label="Living room with fireplace"><span class="tile-label">LIVING ROOM</span></div>
<div class="tile abs" role="img" aria-label="Covered patio with lounge chairs opening to a garden" style="left:350px;top:3428px;width:250px;height:255px;background:linear-gradient(180deg,#d8d8d8 0%,#7f7f7f 60%,#676767 100%)"></div>
<div class="tile abs" role="img" aria-label="White dining room with a pendant lamp" style="left:607px;top:3163px;width:236px;height:520px;background:linear-gradient(180deg,#efefef 0%,#d6d6d6 55%,#464646 100%)"></div>
<div class="tile abs" role="img" aria-label="Bright living room with tall windows and cream seating" style="left:850px;top:3163px;width:252px;height:257px;background:linear-gradient(180deg,#f4f4f4 0%,#dfdfdf 70%,#ababab 100%)"></div>
<div class="tile abs" style="left:850px;top:3428px;width:252px;height:255px;background:linear-gradient(180deg,#9a9a9a,#7e7e7e)" role="img" aria-label="Study room with bookshelves"><span class="tile-label">STUDY ROOM</span></div>

<footer>
  <div class="footer abs"></div>
  <div class="foot-mark abs">CBH</div>
  <p class="foot-text abs">Lorem ipsum dolor sit amet, consectetur adipiscing elit, sed do eiusmod tempor incididunt ut labore et dolore magna aliqua. Quis ipsum suspendisse ultrices gravida. Risus commodo viverra maecenas</p>
  <div class="foot-social abs"><span class="dot-icon"></span><span class="dot-icon"></span><span class="dot-icon"></span><span class="dot-icon"></span></div>
  <div class="foot-col abs" style="left:550px">
    <h4>Helpful Links</h4>
    <ul><li>About Us</li><li>Features</li><li>FAQ's</li><li>Blog</li></ul>
  </div>
  <div class="foot-col abs" style="left:761px">
    <h4>Support</h4>
    <ul><li>Privacy Policy</li><li>Terms of Use</li><li>Support Center</li><li>Contact</li></ul>
  </div>
  <div class="foot-col foot-contact abs" style="left:930px">
    <h4>Contact Us</h4>
    <p>120 Linden Row<br>Harbor Falls, NC 28000</p>
    <p>Phone: (555) 014-2290</p>
    <p>E-Mail: hello@cbh.example</p>
  </div>
  <div class="footer-bar abs">2020 Clara Beth Holloway | All Right Reserved</div>
</footer>

</body>
</html>
```